Web Design for Financial Consulting Company

We need a website design for a financial consulting company "Kelvane Consulting". We build financial models, scenario analysis, handle the budgeting process and provide temporary staffing. I have over 10 years of experience. My Excel expertise and analytical savvy has saved clients over $17 million in profit.

Target Market(s)

Small to medium businesses

Industry/Entity Type

Financial Consulting

Number of Pages Required

4 page

Requirements
Must have
• Professional looking
Nice to have
• A little futuristic looking

```html
<!DOCTYPE html>
<html lang="en">
<head>
<meta charset="UTF-8">
<title>Kelvane Consulting</title>
<link rel="stylesheet" href="https://fonts.googleapis.com/css2?family=Montserrat:ital,wght@0,300;0,400;0,500;0,600;0,700;1,400;1,600&display=swap">
<style>
:root{
  --blue:#00a8f0;
  --blue-light:#29b6f6;
  --navy:#0c3b66;
  --navy-dark:#083056;
  --ink:#222831;
  --muted:#4a4f57;
  --footer:#1c2a3a;
  --white:#ffffff;
  --line:#d9dde2;
}
*{margin:0;padding:0;box-sizing:border-box}
html,body{width:1200px;height:3138px;overflow:hidden}
body{font-family:'Montserrat',sans-serif;color:var(--ink);background:var(--white);position:relative}

/* header */
.site-header{position:absolute;left:0;top:0;width:1200px;height:77px;background:var(--white)}
.brand{position:absolute;left:112px;top:22px;display:flex;align-items:center;gap:10px;white-space:nowrap}
.brand-mark{width:32px;height:32px;background:var(--blue);flex:none}
.brand-name{font-size:21px;font-weight:700;color:var(--navy);letter-spacing:0.5px;line-height:1}
.main-nav{position:absolute;top:30px;font-size:15px;font-weight:500;color:var(--ink);white-space:nowrap}
.btn{position:absolute;display:flex;align-items:center;font-weight:700;font-size:15px;color:var(--white);text-transform:uppercase;white-space:nowrap}
.btn .arrow{position:absolute;right:8px;top:50%;transform:translateY(-50%);width:36px;height:36px;border-radius:50%;display:flex;align-items:center;justify-content:center}
.btn-quote-nav{left:920px;top:16px;width:168px;height:46px;background:var(--blue);justify-content:center}

/* hero */
.hero{position:absolute;left:0;top:77px;width:1200px;height:654px;background:linear-gradient(100deg,#2a1a12 0%,#4a3320 30%,#2d5b5e 60%,#3d6f70 80%,#4a4036 100%)}
.hero-title{position:absolute;left:111px;top:200px;color:var(--white);line-height:1.18}
.hero-title .b{font-weight:700;font-size:46px;display:block}
.hero-title .l{font-weight:300;font-size:56px;display:block}
.hero-text{position:absolute;left:111px;top:378px;width:490px;color:var(--white);font-size:16.5px;line-height:26px}
.btn-hero{left:111px;top:475px;width:211px;height:47px;background:var(--blue);padding-left:29px}
.btn-hero .arrow{background:var(--navy-dark)}
.dots{position:absolute;left:111px;top:545px;display:flex;gap:10px}
.dots span{width:22px;height:22px;border-radius:50%;border:2px solid var(--white)}
.dots span.on{background:var(--white)}

/* services */
.service{position:absolute;top:658px;width:236px;height:237px;background:var(--white);border:1px solid var(--line);border-bottom:5px solid var(--blue);padding:0 12px}
.service.active{background:var(--blue);border-color:var(--blue);border-bottom-color:var(--navy)}
.service .icon{margin-top:24px;width:62px;height:62px}
.service h3{margin-top:12px;font-size:17px;font-weight:600;color:var(--ink);white-space:nowrap}
.service p{margin-top:10px;font-size:14.6px;line-height:26px;color:var(--muted);padding-left:2px;letter-spacing:-0.1px}
.service.active h3,.service.active p{color:var(--white)}

/* about */
.about-bracket{position:absolute;left:111px;top:1034px;width:44px;height:182px;border:9px solid var(--blue);border-right:none}
.eyebrow{font-size:17px;color:var(--blue);font-weight:400}
.about-label{position:absolute;left:167px;top:1028px}
.about-title{position:absolute;left:167px;top:1058px;color:var(--navy);line-height:1.2;white-space:nowrap}
.about-title .b{font-weight:700;font-size:44px;display:block}
.about-title .l{font-weight:300;font-size:52px;display:block}
.about-text{position:absolute;left:110px;top:1245px;width:480px;font-size:17.5px;line-height:29.5px;color:var(--ink)}
.btn-read{left:110px;top:1427px;width:210px;height:47px;background:var(--navy);padding-left:29px}
.btn-read .arrow{background:var(--blue)}
.about-photo{position:absolute;left:622px;top:1035px;width:458px;height:461px;background:linear-gradient(135deg,#1fb3f2,#0d8fd8)}
.about-photo .inner{position:absolute;left:34px;top:34px;width:390px;height:393px;background:linear-gradient(160deg,#3a5a80,#c9d2dc 55%,#8aa7c4)}

/* stats */
.stats{position:absolute;left:0;top:1641px;width:1200px;height:186px;background:linear-gradient(90deg,#0b3a67,#0e4675 50%,#0a3762)}
.stat{position:absolute;top:50px;display:flex;align-items:center}
.stat svg{width:74px;height:80px}
.stat .divider{width:1px;height:76px;background:rgba(255,255,255,.35);margin:0 14px 0 10px}
.stat .txt{font-size:33px;font-weight:700;color:var(--blue-light);line-height:41px;white-space:nowrap}

/* testimonials */
.testimonials{position:absolute;left:0;top:1827px;width:1200px;height:921px;background:linear-gradient(180deg,#fff 0%,#fff 45%,#e9eef4 80%,#dfe6ee 100%)}
.testi-label{position:absolute;left:0;width:1200px;top:1986px;text-align:center}
.testi-title{position:absolute;left:0;width:1200px;top:2012px;text-align:center;color:var(--navy);line-height:56px}
.testi-title .b{font-weight:700;font-size:44px}
.testi-title .l{font-weight:300;font-size:50px}
.testi-card{position:absolute;left:111px;top:2163px;width:978px;height:391px;background:var(--white);border:2px solid var(--line)}
.quote-mark{position:absolute;left:150px;top:2190px;font-size:64px;font-weight:700;font-style:italic;color:var(--blue);line-height:1}
.quote-text{position:absolute;left:145px;top:2238px;width:445px;text-align:center;font-style:italic;font-size:17.5px;line-height:30px;color:var(--muted)}
.quote-name{position:absolute;left:145px;width:445px;top:2442px;text-align:center;font-style:italic;font-weight:600;font-size:19px;color:var(--blue)}
.quote-place{position:absolute;left:145px;width:445px;top:2474px;text-align:center;font-size:17px;color:var(--muted)}
.testi-photo{position:absolute;left:726px;top:2197px;width:323px;height:323px;background:#2fb6ef}
.testi-photo .inner{position:absolute;left:22px;top:22px;width:279px;height:279px;background:linear-gradient(160deg,#6e8fae,#c7d3de 60%,#9fb2c4)}
.btn-view{left:389px;top:2527px;width:210px;height:46px;background:var(--blue);padding-left:29px}
.btn-view .arrow{background:var(--navy-dark)}

/* footer */
.site-footer{position:absolute;left:0;top:2748px;width:1200px;height:390px;background:var(--footer);color:var(--white)}
.footer-brand{position:absolute;left:110px;top:76px;display:flex;align-items:center;gap:10px;white-space:nowrap}
.footer-brand .brand-mark{width:40px;height:40px}
.footer-brand .brand-name{color:var(--white);font-size:22px}
.footer-about{position:absolute;left:110px;top:152px;width:340px;font-size:14px;line-height:25.5px;color:#dfe5ec}
.footer-copy{position:absolute;left:110px;top:275px;font-size:14px;line-height:25.5px;color:#dfe5ec}
.footer-heading{position:absolute;top:70px;font-size:17px;font-weight:600;color:#d8e3ee;width:210px;padding-bottom:10px;border-bottom:2px solid var(--blue)}
.footer-links{position:absolute;left:526px;top:124px;list-style:none;font-size:14px;color:#dfe5ec}
.footer-links li{height:35.5px}
.contact-item{position:absolute;left:831px;display:flex;align-items:center;gap:17px;font-size:13.5px;line-height:20px;color:#dfe5ec;white-space:nowrap}
.contact-item .ic{width:36px;height:36px;border-radius:50%;background:var(--blue);display:flex;align-items:center;justify-content:center;flex:none}
</style>
</head>
<body>

<header class="site-header">
  <div class="brand"><span class="brand-mark"></span><span class="brand-name">KELVANE CONSULTING</span></div>
  <nav>
    <span class="main-nav" style="left:479px">HOME</span>
    <span class="main-nav" style="left:563px">ABOUT US</span>
    <span class="main-nav" style="left:679px">SERVICES</span>
    <span class="main-nav" style="left:790px">CONTACT US</span>
  </nav>
  <a class="btn btn-quote-nav">GET A QUOTE</a>
</header>

<section class="hero" role="img" aria-label="Photo of coin stacks and rising financial bar chart with growth arrow"></section>
<h1 class="hero-title"><span class="b">We build</span><span class="l">Financial Models,</span><span class="b">Scenario Analysis,</span></h1>
<p class="hero-text">Lorem Ipsum is simply dummy text of the printing and typesetting industry. Lorem Ipsum has been the industry's standard dummy text ever since the 1500s</p>
<a class="btn btn-hero">GET A QUOTE<span class="arrow"><svg width="18" height="12" viewBox="0 0 18 12"><path d="M1 6h15M11 1l5 5-5 5" fill="none" stroke="#fff" stroke-width="2"/></svg></span></a>
<div class="dots"><span class="on"></span><span></span><span></span></div>

<div class="service" style="left:111px">
  <svg class="icon" viewBox="0 0 62 62" fill="none" stroke="#1ea7f5" stroke-width="2.4"><path d="M6 44l12-6h14l10 4-2 5H26M6 44v12h10l14-4 22-10-3-4-17 6"/><rect x="22" y="12" width="22" height="22"/><path d="M27 18v10M33 18v10M39 18v10"/></svg>
  <h3>Financial Models</h3>
  <p>Financial analysis, scenario modeling, pricing analysis, projects</p>
</div>
<div class="service" style="left:358px">
  <svg class="icon" viewBox="0 0 62 62" fill="none" stroke="#1ea7f5" stroke-width="2.4"><path d="M8 6h32v50H8z"/><path d="M14 16h18M14 24h10M14 34h20M14 42h14"/><path d="M50 8l6 6-18 30-8 4 2-8z"/></svg>
  <h3>Budgeting Process</h3>
  <p>Financial analysis, scenario modeling, pricing analysis, projects</p>
</div>
<div class="service active" style="left:605px">
  <svg class="icon" viewBox="0 0 62 62" fill="none" stroke="#fff" stroke-width="2.4"><circle cx="18" cy="16" r="12"/><circle cx="18" cy="14" r="4"/><path d="M12 24c2-5 10-5 12 0M16 28v26h6V28"/><circle cx="42" cy="18" r="4"/><circle cx="54" cy="18" r="4"/><path d="M36 30c1-6 11-6 12 0M48 30c1-6 11-6 12 0"/><rect x="30" y="36" width="16" height="18"/><path d="M34 45l4 4 10-12"/></svg>
  <h3>Temporary Staffing</h3>
  <p>Financial analysis, scenario modeling, pricing analysis, projects</p>
</div>
<div class="service" style="left:851px">
  <svg class="icon" viewBox="0 0 62 62" fill="none" stroke="#1ea7f5" stroke-width="2.4"><ellipse cx="34" cy="14" rx="22" ry="7"/><path d="M12 14v34c0 4 10 7 22 7s22-3 22-7V14M12 25c0 4 10 7 22 7s22-3 22-7M12 37c0 4 10 7 22 7s22-3 22-7"/><path d="M4 8l4-4M4 18h4"/></svg>
  <h3>Data Cleansing</h3>
  <p>Financial analysis, scenario modeling, pricing analysis, projects</p>
</div>

<div class="about-bracket"></div>
<p class="eyebrow about-label">About US</p>
<h2 class="about-title"><span class="b">We build</span><span class="l">Financial Models,</span><span class="b">Scenario Analysis,</span></h2>
<p class="about-text">I am an experienced Finance professional who develops strategic financial plans, provides insightful analysis, and supports decision-making. With over 10 years of experience, I have successfully increased profitability for clients by $17M.</p>
<a class="btn btn-read">READ MORE<span class="arrow"><svg width="18" height="12" viewBox="0 0 18 12"><path d="M1 6h15M11 1l5 5-5 5" fill="none" stroke="#fff" stroke-width="2"/></svg></span></a>
<div class="about-photo" role="img" aria-label="Photo of business people reviewing financial charts on a tablet, framed in blue"><div class="inner"></div></div>

<section class="stats">
  <div class="stat" style="left:111px">
    <svg viewBox="0 0 74 80" fill="none" stroke="#1ea7f5" stroke-width="2.5"><path d="M30 6l4 9 10 1-7 7 2 10-9-5-9 5 2-10-7-7 10-1z"/><path d="M4 48l18-6h18l12 6-4 6H28M4 48l6 24h50l6-14-14 0"/><path d="M60 50v24h10V50z"/></svg>
    <span class="divider"></span>
    <span class="txt">10+ years<br>Experience</span>
  </div>
  <div class="stat" style="left:441px">
    <svg viewBox="0 0 74 80" fill="none" stroke="#1ea7f5" stroke-width="2.5"><circle cx="37" cy="20" r="11"/><path d="M18 56c0-14 8-22 19-22s19 8 19 22z"/><circle cx="14" cy="28" r="7"/><circle cx="60" cy="28" r="7"/><path d="M2 52c0-10 5-15 12-15M72 52c0-10-5-15-12-15"/><path d="M10 66l2 4 4 1-3 3 1 4-4-2-4 2 1-4-3-3 4-1zM37 66l2 4 4 1-3 3 1 4-4-2-4 2 1-4-3-3 4-1zM64 66l2 4 4 1-3 3 1 4-4-2-4 2 1-4-3-3 4-1z"/></svg>
    <span class="divider"></span>
    <span class="txt">$17M Clients<br>Successfully</span>
  </div>
  <div class="stat" style="left:806px">
    <svg viewBox="0 0 74 80" fill="none" stroke="#1ea7f5" stroke-width="2.5"><circle cx="34" cy="42" r="30"/><path d="M10 28c8 2 12 8 8 14s4 10 10 12M40 72c0-8 8-10 12-16"/><path d="M56 6c-7 0-12 5-12 12 0 9 12 20 12 20s12-11 12-20c0-7-5-12-12-12z"/><circle cx="56" cy="18" r="4"/></svg>
    <span class="divider"></span>
    <span class="txt">20+ Analysis<br>Supports</span>
  </div>
</section>

<section class="testimonials"></section>
<p class="eyebrow testi-label">Testimonials</p>
<h2 class="testi-title"><span class="b">what says</span><br><span class="l">our happy clients </span><span class="b">about me</span></h2>
<div class="testi-card"></div>
<div class="quote-mark">“</div>
<p class="quote-text">Lorem Ipsum is simply dummy text of the printing and typesetting industry. Lorem Ipsum has been the industry's standard dummy text ever since the 1500s, when an unknown specimen book. It has survived not only five centuries, but also the leap into electronic typesetting,..</p>
<p class="quote-name">Marta Ellison</p>
<p class="quote-place">California</p>
<div class="testi-photo" role="img" aria-label="Portrait photo of a smiling client in an office, framed in blue"><div class="inner"></div></div>
<a class="btn btn-view">VIEW MORE<span class="arrow"><svg width="18" height="12" viewBox="0 0 18 12"><path d="M1 6h15M11 1l5 5-5 5" fill="none" stroke="#fff" stroke-width="2"/></svg></span></a>

<footer class="site-footer">
  <div class="footer-brand"><span class="brand-mark"></span><span class="brand-name">KELVANE CONSULTING</span></div>
  <p class="footer-about">Lorem Ipsum is simply dummy text of the printing and typesetting industry. Lorem Ipsum has been the industry's standard dummy text ever since the 1500s</p>
  <p class="footer-copy">Copyright © Kelvane Consulting 2023.<br>All rights reserved.</p>

  <h4 class="footer-heading" style="left:524px">Quick Links</h4>
  <ul class="footer-links">
    <li>Home</li><li>About Us</li><li>Services</li><li>Contact us</li><li>Privacy Policy</li>
  </ul>

  <h4 class="footer-heading" style="left:831px">Contact Us</h4>
  <div class="contact-item" style="top:120px">
    <span class="ic"><svg width="18" height="18" viewBox="0 0 18 18" fill="none" stroke="#fff" stroke-width="1.6"><path d="M9 1a5 5 0 0 0-5 5c0 4 5 9 5 9s5-5 5-9a5 5 0 0 0-5-5z"/><circle cx="9" cy="6" r="2"/></svg></span>
    <span>Kelvane Consulting<br>46395 enim ipsam voluptatem</span>
  </div>
  <div class="contact-item" style="top:180px">
    <span class="ic"><svg width="18" height="18" viewBox="0 0 18 18" fill="none" stroke="#fff" stroke-width="1.6"><path d="M4 2l3 3-2 2c1 3 3 5 6 6l2-2 3 3-2 3C8 17 1 10 1 4z"/></svg></span>
    <span>Call Us Today!<br>123 456 789</span>
  </div>
  <div class="contact-item" style="top:240px">
    <span class="ic"><svg width="18" height="18" viewBox="0 0 18 18" fill="none" stroke="#fff" stroke-width="1.6"><path d="M2 9l14-7-5 14-2-6z"/></svg></span>
    <span>Email Us<br>info@kelvaneconsulting.com</span>
  </div>
</footer>

</body>
</html>
```